RW Hollis LLC Business Card - Civil Engineering & Consulting Firm

We need a Business Card that is elegant, and masculine.  It is our Professional Civil Engineering & Consulting Company located in San Antonio TX (Not s construction or builder firm- no gears & no tool images please). We provide civil engineering services including  commercial site plans, grading and drainage plans, utility plans, hydraulics and hydrology, land planning, utility coordination, and other general civil engineering services related to commercial and residential development.
We have 2 existing Logos. We would like to convey reliability, strength, trustworthiness and attention to detail.  Blues and orange tones as per logo We are OK with the use of a darker blue in the mix.  We have 2 logo versions - Full Company Name Logo to go on the back of card, & Small Icon Logo for the front w/ personal Info.

Target Market(s)
Architects, Real Estate Developers, Other Strctural Engineers, Surveyers, General Contractors
Industry/Entity Type
Professional Civil Engineering
Contact Information for Business Card
Name, Position, Address, Cell & Office #, email, and company website
Font styles to use
Other font styles liked:
- Avian
Requirements
Should not have
- No Tools, No Gears, no Cranes, or Construction Equipment.

```html
<!DOCTYPE html>
<html lang="en">
<head>
<meta charset="utf-8">
<title>RW Hollis LLC — Business Card</title>
<link href="https://fonts.googleapis.com/css2?family=Raleway:wght@400;500;600;700&display=swap" rel="stylesheet">
<style>
  :root {
    --stage: #363636;
    --card: #1a1a1b;
    --card-back: #151516;
    --pattern-a: #1d1d1f;
    --pattern-b: #2b2b2d;
    --edge-blue: #7fb2e0;
    --brand-blue: #6fa8dc;
    --brand-orange: #e8932f;
    --ink-white: #f1f1f1;
  }
  * { box-sizing: border-box; margin: 0; padding: 0; }
  html, body {
    width: 1200px; height: 801px; overflow: hidden;
    background: var(--stage);
    font-family: "Raleway", sans-serif;
  }
  .stage {
    width: 1200px; height: 801px;
    display: flex; align-items: center; justify-content: center; gap: 40px;
  }
  .card {
    position: relative;
    width: 540px; height: 309px;
    border-radius: 3px;
    border-bottom: 3px solid var(--edge-blue);
    border-left: 2px solid var(--edge-blue);
    overflow: hidden;
  }
  /* Front */
  .card--front { background: var(--card); }
  .brand {
    position: absolute; left: 0; right: 0; top: 52px;
    text-align: center;
  }
  .brand__name {
    display: inline-flex; align-items: center; gap: 10px;
    font-size: 38px; font-weight: 400; letter-spacing: 3px;
    color: var(--brand-blue);
  }
  .brand__square {
    width: 14px; height: 14px; background: var(--brand-blue);
  }
  .brand__tagline {
    margin-top: 6px;
    font-size: 8px; letter-spacing: 4px; text-transform: uppercase;
    color: var(--brand-orange);
  }
  .person { position: absolute; left: 0; right: 0; top: 148px; text-align: center; }
  .person__name {
    font-size: 20px; font-weight: 700; color: var(--brand-blue); letter-spacing: .5px;
  }
  .person__title { font-size: 13px; color: var(--ink-white); margin-top: 2px; }
  .divider {
    position: absolute; left: 30px; right: 30px; top: 212px;
    height: 1px; background: var(--brand-blue);
  }
  .contact {
    position: absolute; left: 30px; top: 226px;
    list-style: none; font-size: 13px; color: var(--ink-white); line-height: 21px;
  }
  .contact li { display: flex; align-items: center; gap: 8px; }
  .contact svg { width: 11px; height: 11px; fill: var(--brand-orange); flex: none; }
  .address {
    position: absolute; right: 30px; top: 226px; text-align: right;
    font-size: 13px; color: var(--ink-white); line-height: 21px; font-style: normal;
  }
  .address__web { color: var(--brand-orange); }
  /* Back */
  .card--back { background: var(--card-back); }
  .back-pattern {
    position: absolute; inset: 0;
    background: linear-gradient(120deg, var(--pattern-a) 0%, var(--pattern-b) 100%);
  }
  .back-brand {
    position: absolute; left: 0; right: 0; top: 50%; transform: translateY(-50%);
    text-align: center;
  }
  .back-brand__name {
    display: inline-block; padding: 8px 14px;
    background: var(--card-back);
    font-size: 20px; font-weight: 600; letter-spacing: 2px; color: var(--brand-orange);
  }
</style>
</head>
<body>
<main class="stage">
  <section class="card card--front">
    <div class="brand">
      <div class="brand__name"><span class="brand__square"></span>RW HOLLIS LLC</div>
      <div class="brand__tagline">Consulting Engineers</div>
    </div>
    <div class="person">
      <div class="person__name">DEAN CARVER</div>
      <div class="person__title">President</div>
    </div>
    <div class="divider"></div>
    <ul class="contact">
      <li><svg viewBox="0 0 12 12"><path d="M3 0h6v12H3z M4 1v9h4V1z"/></svg>555-310-4872</li>
      <li><svg viewBox="0 0 12 12"><path d="M2 1l3 0 1 3-2 1c1 2 2 3 3 3l1-2 3 1v3c-6 0-9-4-9-9z"/></svg>555-310-4872</li>
      <li><svg viewBox="0 0 12 12"><path d="M0 2h12v8H0z M1 3l5 4 5-4z" fill-rule="evenodd"/></svg>info@rwhollisconsulting.com</li>
    </ul>
    <address class="address">
      1840 Harbor Ridge Drive<br>
      Seal Cove CA 92000<br>
      <span class="address__web">www.rwhollisconsulting</span>
    </address>
  </section>

  <section class="card card--back">
    <div class="back-pattern" role="img" aria-label="Repeating embossed pattern of the company monogram in dark tones"></div>
    <div class="back-brand">
      <span class="back-brand__name">RW HOLLIS</span>
    </div>
  </section>
</main>
</body>
</html>
```